Need Blister Card Packaging Design for Our New Product

Need a blister card design for our new product which is 'self-cleaning slicker brush.
I have attached a sample for your reference.
The sample & color of the product is attached along with.
Blister card design should match the color of the product.

```html
<!DOCTYPE html>
<html lang="en">
<head>
<meta charset="UTF-8">
<title>Self-Cleaning Slicker Brush – Blister Card</title>
<link href="https://fonts.googleapis.com/css2?family=Open+Sans:wght@400;600;700;800&family=Arimo:wght@400;700&display=swap" rel="stylesheet">
<style>
  :root{
    --stage:#eceef0;
    --card:#eeeff1;
    --sky:#7cc4e8;
    --sky-light:#a9daf2;
    --navy:#1d2a3a;
    --ink:#2a2f36;
    --text:#3b3f45;
    --white:#ffffff;
    --blister:#e0663a;
    --placeholder-light:#c9d3da;
    --placeholder-mid:#8e9aa4;
    --shadow:rgba(0,0,0,.28);
  }
  *{box-sizing:border-box;margin:0;padding:0}
  html,body{width:1200px;height:996px;overflow:hidden;background:var(--stage)}
  .stage{position:relative;width:1200px;height:996px}
  .card{position:absolute;top:120px;width:438px;height:760px;border-radius:20px;background:var(--card);overflow:hidden;box-shadow:8px 10px 14px var(--shadow);font-family:"Arimo",Arial,sans-serif;color:var(--text)}
  .card--front{left:93px}
  .card--back{left:640px}
  .card__art{position:absolute;inset:0;width:100%;height:100%}
  .hang-slot{position:absolute;top:26px;left:176px;width:86px;height:18px;border-radius:9px;background:#b8bcc2}

  /* front */
  .front__kicker{position:absolute;top:64px;left:0;right:0;text-align:center;font-family:"Open Sans",sans-serif;font-weight:400;font-size:27px;letter-spacing:1px;color:var(--navy)}
  .front__title{position:absolute;top:96px;left:0;right:0;text-align:center;font-family:"Open Sans",sans-serif;font-weight:800;font-size:40px;color:var(--navy);letter-spacing:.5px}
  .size-badge{position:absolute;top:0;left:351px;width:60px;height:63px}
  .size-badge span{position:absolute;top:10px;left:0;right:0;text-align:center;font-family:"Open Sans",sans-serif;font-weight:700;font-size:8px;line-height:10px;color:var(--sky-light)}
  .features{position:absolute;top:216px;left:24px;width:150px;list-style:none}
  .features li{position:relative;padding-left:14px;font-size:15px;line-height:19px;color:var(--text);margin-bottom:14px}
  .features li::before{content:"";position:absolute;left:0;top:6px;width:7px;height:7px;border-radius:50%;background:var(--sky)}
  .callout{position:absolute;left:346px;width:72px;height:72px;border-radius:50%;border:3px solid var(--navy);overflow:hidden;background:linear-gradient(135deg,var(--placeholder-light),var(--placeholder-mid))}
  .callout--grip{top:186px}
  .callout--button{top:322px}
  .callout__label{position:absolute;left:332px;width:100px;text-align:center;font-family:"Open Sans",sans-serif;font-weight:700;font-size:6px;line-height:7px;color:var(--navy)}
  .callout__label--grip{top:263px}
  .callout__label--button{top:399px}
  .dog-photo{position:absolute;left:0;bottom:0;width:111px;height:184px;background:linear-gradient(160deg,#8e9398,#d9dde0 55%,#5f6468)}

  /* back */
  .back__title{position:absolute;top:63px;left:0;right:0;text-align:center;font-family:"Open Sans",sans-serif;font-weight:800;font-size:23px;color:var(--navy)}
  .how-to{position:absolute;top:124px;left:38px;width:370px;height:132px;border:2px solid var(--navy);border-radius:8px;background:rgba(255,255,255,.55)}
  .pill{display:inline-block;background:var(--sky);color:var(--navy);font-family:"Open Sans",sans-serif;font-weight:700;border-radius:10px;border:1.5px solid var(--navy)}
  .how-to__tab{position:absolute;top:-11px;left:50%;transform:translateX(-50%);font-size:14px;padding:1px 14px;white-space:nowrap}
  .how-to__step{position:absolute;top:20px;width:130px;height:76px;border-radius:10px;background:linear-gradient(135deg,var(--placeholder-light),var(--placeholder-mid))}
  .how-to__step--one{left:20px}
  .how-to__step--two{right:20px}
  .how-to__caption{position:absolute;bottom:6px;left:0;right:0;text-align:center;font-size:9px;line-height:10px;color:var(--text)}
  .section-head{position:absolute;left:0;right:0;text-align:center}
  .section-head .pill{font-size:11px;padding:2px 18px}
  .section-head--instructions{top:292px}
  .section-head--warning{top:484px;text-align:left;left:22px}
  .instructions{position:absolute;top:320px;left:22px;width:365px;list-style:none}
  .instructions li{position:relative;padding-left:12px;font-size:11.5px;line-height:13.3px;margin-bottom:3px;color:var(--text)}
  .instructions li::before{content:"";position:absolute;left:0;top:4px;width:6px;height:6px;border-radius:50%;background:var(--sky)}
  .warnings{position:absolute;top:511px;left:22px;width:368px;list-style:none}
  .warnings li{font-size:11.5px;line-height:13.3px;margin-bottom:2px;color:var(--text)}
  .origin{position:absolute;left:38px;top:672px;text-align:center;font-size:11px;color:var(--ink)}
  .origin__mark{display:block;width:30px;height:30px;margin:0 auto 4px}
</style>
</head>
<body>
<main class="stage">

  <section class="card card--front" aria-label="Front of blister card">
    <svg class="card__art" viewBox="0 0 438 760" aria-hidden="true">
      <path d="M0 0H438V150C330 150 260 110 150 115 80 118 30 140 0 150Z" fill="var(--sky)"/>
      <path d="M0 150C60 128 130 118 200 122 290 128 360 150 438 160V170C350 160 280 140 200 136 120 132 50 150 0 168Z" fill="var(--white)"/>
      <path d="M0 190C120 160 240 160 330 180 380 192 410 200 438 198V215C400 216 370 205 320 196 240 180 130 178 0 200Z" fill="var(--navy)"/>
      <path d="M438 185C360 190 320 205 300 230 340 212 390 205 438 205Z" fill="var(--navy)"/>
      <path d="M0 525C100 500 180 510 240 545 200 520 110 510 0 535Z" fill="var(--navy)"/>
      <path d="M0 590C110 570 210 590 300 630 360 655 410 660 438 655V760H0Z" fill="var(--sky)"/>
      <path d="M90 590C190 580 270 610 340 650 380 670 420 670 438 666V680C410 686 370 680 320 660 250 630 180 600 90 590Z" fill="var(--white)"/>
      <path d="M191 184Q191 176 199 176H279Q287 176 287 184V455Q287 463 295 463H368Q376 463 376 471V656Q376 664 368 664H75Q67 664 67 656V471Q67 463 75 463H183Q191 463 191 455Z" fill="none" stroke="var(--blister)" stroke-width="1.5"/>
      <g fill="none" stroke="var(--navy)" stroke-width="2">
        <path d="M382 275V304H310"/>
        <path d="M382 411V463H318"/>
      </g>
      <path d="M310 299 300 304 310 309Z" fill="var(--navy)"/>
      <path d="M318 458 308 463 318 468Z" fill="var(--navy)"/>
    </svg>
    <div class="hang-slot"></div>
    <div class="size-badge">
      <svg viewBox="0 0 60 63" width="60" height="63" aria-hidden="true"><path d="M0 0H60V63L30 52 0 63Z" fill="var(--navy)"/></svg>
      <span>FOR LARGE<br>&amp; MEDIUM<br>DOGS</span>
    </div>
    <p class="front__kicker">SELF CLEANING</p>
    <h1 class="front__title">BRUSH.BLISTER</h1>
    <ul class="features">
      <li>Removes matts and tangles easily</li>
      <li>Leaves your dog's coat soft &amp; shiny</li>
      <li>Comfortable ergonomic handle</li>
      <li>Unique self-cleaning brush action</li>
    </ul>
    <div class="callout callout--grip" role="img" aria-label="Close-up photo of the rubberised brush handle"></div>
    <p class="callout__label callout__label--grip">RUBBERTED FOR EXTRA<br>COMFORTABLE GRIP</p>
    <div class="callout callout--button" role="img" aria-label="Close-up photo of the self-cleaning push button"></div>
    <p class="callout__label callout__label--button">SELF-CLEANING<br>PUSH BUTTONVVVVV</p>
    <div class="dog-photo" role="img" aria-label="Photo of a husky being brushed with the slicker brush"></div>
  </section>

  <section class="card card--back" aria-label="Back of blister card">
    <svg class="card__art" viewBox="0 0 438 760" aria-hidden="true">
      <path d="M0 0H438V110C360 118 280 108 200 104 120 100 50 110 0 120Z" fill="var(--sky)"/>
      <path d="M0 300C60 270 120 255 200 258 120 250 50 262 0 280Z" fill="var(--navy)"/>
      <path d="M0 270C90 245 170 240 240 250 170 235 80 240 0 258Z" fill="var(--navy)"/>
      <path d="M438 250C400 265 360 275 300 276 360 282 410 278 438 270Z" fill="var(--navy)"/>
      <path d="M0 730C80 716 160 700 250 680 330 664 390 656 438 650V760H0Z" fill="var(--sky)"/>
      <path d="M0 706C100 704 200 690 300 672 370 660 410 654 438 650 400 670 330 678 260 690 160 710 80 722 0 730Z" fill="var(--white)"/>
    </svg>
    <div class="hang-slot"></div>
    <h2 class="back__title">SELF-CLEANING SLICKER BRUSH</h2>
    <div class="how-to">
      <span class="pill how-to__tab">How To Use</span>
      <div class="how-to__step how-to__step--one" role="img" aria-label="Illustration of the brush with bristles extended"></div>
      <div class="how-to__step how-to__step--two" role="img" aria-label="Illustration of the button pressed and bristles retracted"></div>
      <p class="how-to__caption">Self-cleaning bristles retract with<br>a push of a button, that was easy!</p>
    </div>
    <div class="section-head section-head--instructions"><span class="pill">INSTRUCTIONS</span></div>
    <ul class="instructions">
      <li>All-in-One Self Cleaning Slicker Dog and Cat Brush is great for long, medium, short, thick, wiry, or curly hair.</li>
      <li>Grooms and massages for a healthy coat, increases blood circulation, effectively designed to penetrate deep into the coat, and will not damage or scratch your pet's skin.</li>
      <li>Self cleaning - no more stabbed fingers. Simply click the button to clean the brush. So easy! Features a durable and comfortable handle.</li>
      <li>Keep your pet looking and feeling great!</li>
    </ul>
    <div class="section-head section-head--warning"><span class="pill">Warning</span></div>
    <ol class="warnings">
      <li>1.Please keep the grooming tool away from fire and high temperature.</li>
      <li>2.Please keep the grooming tool out of your pet's or a child's reach.</li>
      <li>3.Please keep the grooming tool clean after use. Always keep it dry after washing.</li>
      <li>4.Please be careful when using the grooming tool and avoid improper use which could cause injuries to your pet.</li>
    </ol>
    <div class="origin">
      <svg class="origin__mark" viewBox="0 0 30 30" aria-hidden="true">
        <g fill="none" stroke="var(--ink)" stroke-width="3" stroke-linejoin="round">
          <path d="M10 11 15 4 19 10"/>
          <path d="M22 15 26 22H18"/>
          <path d="M12 24H4L8 17"/>
        </g>
        <g fill="var(--ink)">
          <path d="M16 8 22 9 21 14Z"/>
          <path d="M18 19 15 24 18 27Z"/>
          <path d="M5 15 10 13 11 18Z"/>
        </g>
      </svg>
      Made in China
    </div>
  </section>

</main>
</body>
</html>
```